Marwick Ostrand Law website for a law firm

modern clean website for a small boutique law firm. Based in Sacramento, CA and the Bay Area. Practice areas of Family Law, Civil litigation, and Criminal Defense. We already have a logo design as well as attorney pictures to include on page.
Would like images of California included on site.
Would like site to go with Logo that is already designed...blue/grey/white colors.

Industry/Entity Type

Law Firm

Number of Pages Required

5+ page

Requirements
Must have
• I already have several pages of content drafted. Just need the pages with images to input content. Must be clean and modern feel. Want it to reflect California and small boutique feel that is provided personalized legal attention.
• Must have a page where I can blog or post articles on.

```html
<!DOCTYPE html>
<html lang="en">
<head>
<meta charset="utf-8">
<title>Marwick Ostrand Law</title>
<link rel="stylesheet" href="https://fonts.googleapis.com/css2?family=Montserrat:wght@400;500;600;700&family=Open+Sans:wght@400;600;700&family=Roboto+Condensed:wght@400;700&family=Noto+Serif:ital@1&display=swap">
<style>
:root{
  --blue:#2f86d0;
  --blue-dark:#2a6fb3;
  --ink:#2b2b2b;
  --text:#666;
  --muted:#999;
  --topbar:#3a3a3a;
  --footer:#393939;
  --navy:#2c3446;
  --tan:#a9773f;
  --dark-band:#2e2e2e;
  --line:#e3e3e3;
  --white:#fff;
}
*{margin:0;padding:0;box-sizing:border-box}
html,body{width:1200px;height:3462px;overflow:hidden;background:var(--white)}
body{font-family:"Open Sans",sans-serif;color:var(--text);position:relative}
.abs{position:absolute}
.section{position:absolute;left:0;width:1200px}

/* top bar */
.topbar{top:0;height:35px;background:var(--topbar);color:#cfcfcf;font-size:11px}
.social{left:95px;top:8px;display:flex;gap:6px}
.social span{width:19px;height:19px;border-radius:50%;background:#8a8a8a;display:block}
.topbar .mail{left:718px;top:9px}
.topbar .mail b{color:#fff;font-weight:400}
.topbar .reg{left:962px;top:9px}
.topbar .login{left:1058px;top:9px}

/* header */
.header{top:35px;height:92px;background:var(--white);border-bottom:1px solid var(--line)}
.logo{left:84px;top:20px;font-family:"Montserrat",sans-serif;font-size:44px;font-weight:500;color:var(--blue);letter-spacing:-1px;line-height:50px}
.nav{left:396px;top:32px;display:flex;align-items:center;font-family:"Montserrat",sans-serif;font-size:15px;color:var(--ink)}
.nav a{color:inherit;text-decoration:none;margin-right:38px}
.nav .active{background:var(--blue);color:#fff;padding:6px 16px;margin-right:20px}
.callbox{left:885px;top:0;height:92px;border-left:1px solid var(--line);padding-left:52px;padding-top:20px}
.callbox .icon{position:absolute;left:18px;top:22px}
.callbox small{display:block;font-size:14px;color:var(--muted);letter-spacing:.5px}
.callbox strong{font-family:"Montserrat",sans-serif;font-size:23px;color:var(--ink);font-weight:500}

/* hero */
.hero{top:127px;height:466px;background:linear-gradient(100deg,#4a3a30 0%,#2a2622 35%,#3d3530 60%,#6a5546 85%,#2b2520 100%);text-align:center;color:#fff}
.hero h1{position:absolute;top:150px;left:0;width:100%;font-family:"Montserrat",sans-serif;font-size:41px;font-weight:700}
.hero p{position:absolute;top:215px;left:340px;width:520px;font-size:14px;line-height:22px}
.btn-outline{position:absolute;top:293px;left:497px;width:189px;height:46px;border:1px solid var(--blue);color:#fff;font-size:15px;line-height:44px}

/* about */
.about{top:593px;height:572px}
.about h2{left:110px;top:72px;font-family:"Montserrat",sans-serif;font-size:41px;font-weight:500;color:var(--ink)}
.about .copy{left:110px;top:148px;width:465px;font-size:11px;line-height:22px;color:#555}
.about .copy p{margin-bottom:14px}
.signature{left:110px;top:370px;width:130px;height:62px;background:linear-gradient(135deg,#f4f4f4,#e6e6e6)}
.about-photo{left:615px;top:67px;width:423px;height:433px;background:linear-gradient(160deg,#5a3e28 0%,#2b211a 45%,#6b5238 75%,#1d1713 100%)}

/* practice panels */
.practice{top:1165px;height:439px}
.panel{position:absolute;top:0;width:600px;height:439px;text-align:center;color:#fff}
.panel.civil{left:0;background:linear-gradient(135deg,#3a4256,var(--navy) 60%,#1f2533)}
.panel.criminal{left:600px;background:linear-gradient(135deg,#c08b4c,var(--tan) 55%,#7e5428)}
.panel h3{position:absolute;top:80px;width:100%;font-family:"Montserrat",sans-serif;font-size:44px;font-weight:700}
.panel p{position:absolute;top:163px;left:130px;width:340px;font-size:12.5px;line-height:21px}
.btn-white{position:absolute;top:313px;left:227px;width:145px;height:41px;background:#fff;color:var(--ink);font-size:12px;font-weight:700;line-height:41px}
.notch{left:585px;top:0}

/* reviews + services */
.reviews{top:1604px;height:688px}
.label{position:absolute;border-left:5px solid var(--blue);padding-left:18px}
.label em{display:block;font-family:"Noto Serif",serif;font-size:16px;color:#777}
.label b{display:block;font-family:"Roboto Condensed",sans-serif;font-size:22px;color:var(--ink);letter-spacing:.5px}
.avatar-lg{left:110px;top:193px;width:103px;height:103px;border-radius:50%;background:linear-gradient(#7a5a44,#3c2a20)}
.person{left:237px;top:226px}
.person b{display:block;font-family:"Roboto Condensed",sans-serif;font-size:14px;color:var(--ink)}
.person small{font-size:10px;color:var(--muted);letter-spacing:.5px}
.quote-mark{left:110px;top:310px;font-family:"Noto Serif",serif;font-size:56px;color:#ddd;line-height:1}
.quote{left:110px;top:330px;width:310px;font-family:"Noto Serif",serif;font-style:italic;font-size:14px;line-height:24px;color:#888}
.dots{left:240px;top:545px;display:flex;gap:6px}
.dots span{width:10px;height:10px;border-radius:50%;border:1px solid #aaa}
.dots .on{background:var(--blue);border-color:var(--blue)}
.tabs{left:445px;top:196px;width:645px;height:44px;border-bottom:1px solid var(--line);display:flex;font-family:"Roboto Condensed",sans-serif;font-size:12px;color:var(--ink)}
.tabs span{flex:1;text-align:center;line-height:44px;border-right:1px solid var(--line)}
.tabs span:last-child{border-right:none}
.tabs .on{color:var(--blue);border-bottom:2px solid var(--blue)}
.service-title{left:445px;top:268px;font-family:"Roboto Condensed",sans-serif;font-weight:700;font-size:14px;color:var(--ink)}
.service-photo{left:445px;top:302px;width:198px;height:140px;background:linear-gradient(120deg,#6b4a34,#3a2a22 50%,#8d7a66)}
.service-body{left:668px;top:305px;width:422px;font-size:11px;line-height:19px;color:#888}
.service-body h4{font-family:"Roboto Condensed",sans-serif;color:var(--blue);font-size:14px;font-weight:400;margin-bottom:12px}
.service-body p{margin-bottom:10px}
.service-more{left:445px;top:465px;width:645px;font-size:11px;line-height:19px;color:#888}

/* consultation */
.consult{top:2292px;height:512px;background:linear-gradient(120deg,#3a3a3a,var(--dark-band) 50%,#242424);color:#fff;text-align:center}
.consult h2{position:absolute;top:58px;width:100%;font-family:"Montserrat",sans-serif;font-size:35px;font-weight:500}
.consult p{position:absolute;top:125px;left:260px;width:680px;font-size:14px;line-height:25px}
.field{position:absolute;background:#fff;color:#999;font-size:12px;text-align:left;padding:8px 14px}
.btn-blue{position:absolute;top:417px;left:510px;width:180px;height:52px;background:var(--blue);color:#fff;font-family:"Montserrat",sans-serif;font-size:15px;font-weight:600;line-height:52px}

/* client testimonials */
.clients{top:2804px;height:515px;text-align:center}
.clients h2{position:absolute;top:80px;width:100%;font-family:"Montserrat",sans-serif;font-size:35px;font-weight:500;color:var(--ink);letter-spacing:.5px}
.bubble{position:absolute;text-align:left;color:#fff;font-size:15px;line-height:28px;padding:40px 40px}
.bubble.blue{left:192px;top:176px;width:428px;height:130px;background:var(--blue)}
.bubble.dark{left:598px;top:199px;width:428px;height:136px;background:#2d2d2d;padding-top:28px}
.tail{position:absolute}
.arrow-circle{position:absolute;top:281px;width:44px;height:44px;border-radius:50%;border:1px solid #ddd}
.author{position:absolute;text-align:left;display:flex;align-items:center;gap:14px}
.author .av{width:40px;height:40px;border-radius:50%;background:linear-gradient(#b99a80,#5b4536)}
.author b{display:block;font-family:"Montserrat",sans-serif;font-weight:500;font-size:16px;color:var(--ink)}
.author small{font-size:12px;color:var(--muted)}

/* footer */
.footer{top:3319px;height:143px;background:var(--footer);color:#bbb;text-align:center;font-size:13px}
.footer .links{position:absolute;top:36px;width:100%;font-size:14px}
.footer .links span{margin:0 22px}
.footer .contact{position:absolute;top:70px;width:100%}
.footer .copy{position:absolute;top:103px;width:100%;font-size:12px;color:#888}
</style>
</head>
<body>

<div class="section topbar">
  <div class="abs social" aria-label="Social links"><span></span><span></span><span></span><span></span></div>
  <div class="abs mail">✉ Email: <b>info@molaw.com</b></div>
  <div class="abs reg">Register</div>
  <div class="abs login">Login</div>
</div>

<header class="section header">
  <div class="abs logo">MOLAW</div>
  <nav class="abs nav"><a>Home</a><a>About Us</a><a class="active">Practice Areas ▾</a><a>Contact Us</a></nav>
  <div class="abs callbox">
    <svg class="icon" width="22" height="42" viewBox="0 0 22 42"><rect x="1.5" y="1.5" width="19" height="39" rx="3" fill="none" stroke="#2f86d0" stroke-width="3"/><rect x="5" y="7" width="12" height="24" fill="#2f86d0"/><circle cx="11" cy="35.5" r="2" fill="#2f86d0"/></svg>
    <small>CALL US ON:</small>
    <strong>07700-900412</strong>
  </div>
</header>

<section class="section hero" role="img" aria-label="Photo of attorneys meeting with a client">
  <h1>Small Boutique Law Firm</h1>
  <p>Based in Sacramento, CA and the Bay Area. Practice areas of Family Law, Civil litigation, and Criminal Defense.</p>
  <div class="btn-outline">Free Consultation</div>
</section>

<section class="section about">
  <h2 class="abs">Marwick Ostrand Law</h2>
  <div class="abs copy">
    <p>Our attorneys give every client direct, personal attention from the first call to the final ruling. We listen closely, explain each option in plain words, and build a clear plan around your goals. From family matters to complex disputes, we stand beside you at every step and keep you informed as your case moves forward in the courts.</p>
    <p>We serve clients across Sacramento and the Bay Area with focused, practical counsel. Our small team means your case is never handed off, and you always know who is working on it and why each decision matters.</p>
  </div>
  <div class="abs signature" role="img" aria-label="Handwritten signature of the founding attorney"></div>
  <div class="abs about-photo" role="img" aria-label="Photo of scales of justice on books with a gavel"></div>
</section>

<section class="section practice">
  <div class="panel civil" role="img" aria-label="Courthouse columns background">
    <h3>Civil Litigation</h3>
    <p>We guide clients through contract disputes, property claims and business conflicts with careful preparation, steady advocacy and honest advice about the risks and likely outcomes of every path open to you in court.</p>
    <div class="btn-white">More Details</div>
  </div>
  <div class="panel criminal" role="img" aria-label="Statue of Lady Justice background">
    <h3>Criminal Defense</h3>
    <p>When your freedom is at stake, we move quickly to protect your rights, examine the evidence and build a strong defense, standing with you from the first hearing through trial and any appeal that may follow.</p>
    <div class="btn-white">More Details</div>
  </div>
  <svg class="abs notch" width="30" height="15" viewBox="0 0 30 15"><polygon points="0,0 30,0 15,15" fill="#fff"/></svg>
</section>

<section class="section reviews">
  <div class="label" style="left:110px;top:92px"><em>Testimonials</em><b>WHAT PEOPLE SAY</b></div>
  <div class="abs avatar-lg" role="img" aria-label="Client portrait"></div>
  <div class="abs person"><b>JOHN DOE</b><small>CEO, LARKSPUR</small></div>
  <div class="abs quote-mark">“</div>
  <p class="abs quote">At vero eos et accusamus et iusto odio dignissimos ducimus qui blanditiis praesentium voluptatum deleniti atque corrupti quos dolores et quas molestias excepturi sint occaecati cupiditate, similique sunt in culpa qui officia deserunt mollitia.</p>
  <div class="abs dots"><span></span><span class="on"></span><span></span></div>

  <div class="label" style="left:445px;top:92px"><em>We offer a Broad Range</em><b>LAW SERVICES</b></div>
  <div class="abs tabs"><span class="on">CRIMINAL LAW</span><span>LEGAL ADVICE</span><span>TRAFFIC OFFENSE</span><span>PERSONAL INJURY</span></div>
  <div class="abs service-title">LEGAL REPRESENTATION IN LITIGATION CASES</div>
  <div class="abs service-photo" role="img" aria-label="Photo of an attorney advising a client"></div>
  <div class="abs service-body">
    <h4>CRIMINAL LAW</h4>
    <p>We review every charge closely, question weak evidence and seek the fairest result, whether through dismissal, a reduced plea or a firm defense at trial.</p>
    <p>Each client receives a direct line to their attorney and regular updates.</p>
  </div>
  <p class="abs service-more">Our team has handled cases in state and federal courts throughout Northern California. We prepare each matter as if it will go to trial, which gives our clients real strength at the table when a settlement or plea is offered.</p>
</section>

<section class="section consult" role="img" aria-label="Dark photo background of a client meeting">
  <h2>Free Case Consultation</h2>
  <p>Tell us about your situation and one of our attorneys will reach out within one business day to talk through your options at no cost.</p>
  <div class="field" style="left:230px;top:193px;width:242px;height:37px">Name</div>
  <div class="field" style="left:482px;top:193px;width:242px;height:37px">Email</div>
  <div class="field" style="left:734px;top:193px;width:243px;height:37px">Phone</div>
  <div class="field" style="left:230px;top:245px;width:747px;height:143px">Message</div>
  <div class="btn-blue">SUBMIT NOW</div>
</section>

<section class="section clients">
  <h2>Client Testimonials</h2>
  <div class="arrow-circle" style="left:104px"></div>
  <div class="arrow-circle" style="left:1092px"></div>
  <div class="bubble blue">Lorem ipsum dolor sit amet, consectetur adipisicing elit. Enim, delectus atque odit esse harum! Saepe!</div>
  <svg class="tail" style="left:480px;top:306px" width="26" height="22" viewBox="0 0 26 22"><polygon points="0,0 26,0 0,22" fill="#2f86d0"/></svg>
  <div class="bubble dark">Lorem ipsum dolor sit amet, consectetur adipisicing elit. Enim, delectus atque odit esse harum! Saepe!</div>
  <svg class="tail" style="left:888px;top:335px" width="26" height="22" viewBox="0 0 26 22"><polygon points="0,0 26,0 0,22" fill="#2d2d2d"/></svg>
  <div class="author" style="left:218px;top:330px"><div class="av" role="img" aria-label="Client portrait"></div><div><b>John Doe</b><small>Web designer</small></div></div>
  <div class="author" style="left:620px;top:356px"><div class="av" role="img" aria-label="Client portrait"></div><div><b>Jessica Doe</b><small>Developer</small></div></div>
</section>

<footer class="section footer">
  <div class="links"><span>Terms of use</span>|<span>Privacy statement</span>|<span>Refund policy</span></div>
  <div class="contact">Email: ✉ info@marwickostrandlaw.com &nbsp;|&nbsp; Phone: ✆ +1 (555) 014-2290</div>
  <div class="copy">Copyright ©2017 MO Law. All Right Reserved</div>
</footer>

</body>
</html>
```